Poster Design Project

We are a pizzeria based in Sydney CBD. Please see attached file for new website, do not use the current website look to make your graphic design.

We want to run a promotional campaign called " Crust Carnival".

Crust Carnival
$9 Pizza

Crispy & fresh dough topped with mouth watering mozzarella cheese, sprinkled with oregano and finished with fresh basil.

takeaway & eat in only
Medium Pizza Only (11 inch)

Target Market(s)

It is the lunch crowd in sydney cbd, predominately male but some female too. targeting the office workers.

Industry/Entity Type

Graphic Design

Requirements
Must have
• We are an Italian Pizzeria, so we would like an italian look and feel
our unique advantage is authentic and delicious thin crispy pizza
we want a nostalgic look and feel
some examples are attached of colours and style we like
Nice to have
• I can send you via email files to show you what the new website will look like

```html
<!DOCTYPE html>
<html lang="en">
<head>
<meta charset="utf-8">
<title>Crust Carnival – $9 Pizza</title>
<link rel="stylesheet" href="https://fonts.googleapis.com/css2?family=Yesteryear&family=Kalam:wght@400;700&family=Pangolin&family=Yanone+Kaffeesatz:wght@300;400;500&display=swap">
<style>
  :root {
    --bg-deep: #1a1210;
    --crust-brown: #5a3a26;
    --sauce-red: #7a2a1c;
    --cheese: #8a6f52;
    --basil: #2f3a22;
    --price-red: #f01414;
    --body-white: #ffffff;
    --copy-green: #17961a;
    --flag-green: #2f8a3c;
    --flag-white: #f4f4f0;
    --flag-red: #e0352b;
    --tag-sage: #6f8a72;
    --tag-rose: #b02a3c;
  }
  html, body {
    margin: 0;
    padding: 0;
    overflow: hidden;
    background: var(--bg-deep);
  }
  .poster {
    position: relative;
    width: 960px;
    height: 1200px;
    overflow: hidden;
    background: var(--bg-deep);
  }
  .pizza-photo {
    position: absolute;
    inset: 0;
    background:
      radial-gradient(ellipse at 85% 38%, var(--sauce-red) 0%, transparent 22%),
      radial-gradient(ellipse at 20% 50%, var(--basil) 0%, transparent 25%),
      radial-gradient(ellipse at 50% 70%, var(--cheese) 0%, transparent 40%),
      radial-gradient(ellipse at 30% 15%, var(--sauce-red) 0%, transparent 30%),
      linear-gradient(160deg, var(--crust-brown), var(--sauce-red) 55%, var(--crust-brown));
  }
  .vignette {
    position: absolute;
    inset: 0;
    background:
      radial-gradient(ellipse 48% 46% at 50% 50%, rgba(20,14,12,0.72) 60%, rgba(20,14,12,0.25) 100%);
  }
  .line {
    position: absolute;
    left: 0;
    width: 960px;
    text-align: center;
    margin: 0;
    white-space: nowrap;
  }
  .title {
    top: 140px;
    left: 16px;
    font-family: "Yesteryear", cursive;
    font-size: 124px;
    line-height: 1.2;
    font-weight: 400;
    background: linear-gradient(180deg, var(--flag-green) 15%, var(--flag-white) 52%, var(--flag-red) 88%);
    -webkit-background-clip: text;
    background-clip: text;
    color: transparent;
  }
  .price {
    top: 334px;
    left: -10px;
    font-family: "Pangolin", cursive;
    font-size: 66px;
    line-height: 1;
    color: var(--price-red);
  }
  .details {
    position: absolute;
    top: 444px;
    left: 0;
    width: 944px;
    text-align: center;
    margin: 0;
    font-family: "Yanone Kaffeesatz", sans-serif;
    font-weight: 500;
    font-size: 50px;
    line-height: 44px;
    color: var(--body-white);
  }
  .description {
    position: absolute;
    top: 614px;
    left: 0;
    width: 944px;
    text-align: center;
    margin: 0;
    font-family: "Yanone Kaffeesatz", sans-serif;
    font-weight: 500;
    font-size: 56px;
    line-height: 49px;
    color: var(--copy-green);
  }
  .tagline-top {
    top: 900px;
    left: 12px;
    font-family: "Yanone Kaffeesatz", sans-serif;
    font-weight: 300;
    font-size: 82px;
    letter-spacing: -3px;
    line-height: 1;
    transform: scaleY(1.3);
    background: linear-gradient(180deg, var(--tag-sage) 30%, #c9c9c0 100%);
    -webkit-background-clip: text;
    background-clip: text;
    color: transparent;
  }
  .tagline-bottom {
    top: 990px;
    left: 20px;
    font-family: "Kalam", cursive;
    font-size: 75px;
    line-height: 1.1;
    background: linear-gradient(180deg, #d9a8b0 20%, var(--tag-rose) 90%);
    -webkit-background-clip: text;
    background-clip: text;
    color: transparent;
  }
</style>
</head>
<body>
  <main class="poster">
    <div class="pizza-photo" role="img" aria-label="Close-up photo of a thin crust margherita pizza with tomato, mozzarella, olives and basil"></div>
    <div class="vignette"></div>

    <h1 class="line title">Crust Carnival</h1>
    <p class="line price">$ 9 Pizza</p>

    <p class="details">Take Out and Eat In ONLY<br>Medium Pizza<br>(11 inch)</p>

    <p class="description">Crispy &amp; fresh dough topped with<br>mouth watering mozzarella cheese,<br>sprinkled with oregano,<br>and finished with fresh basil.</p>

    <p class="line tagline-top">Try our authentic and delicious</p>
    <p class="line tagline-bottom">thin crispy pizza</p>
  </main>
</body>
</html>
```